Create a business promotion flyer to leave in customer mailboxes. We are a bulk petroleum supplier, servicing any industry that requires diesel. Base in griffith NSW, servicing griffith area and surrounds.

Business Name - Terra Diesel
Fuel@terradiesel-example.com.au
Marco - 0412 309 768 mpellucci@terradiesel-example.com.au
Liam - 0431 672 095 lhartwell@terradiesel-example.com.au
Simon - 0465 218 347 sbrack@terradiesel-example.com.au
Office 02 6931 7852

Bulk Fuel deliveries.
Oils & lubricants
Local Family owned business

```html
<!DOCTYPE html>
<html lang="en">
<head>
<meta charset="utf-8">
<title>Terra Diesel – Bulk Petroleum Supplier</title>
<link href="https://fonts.googleapis.com/css2?family=Montserrat:wght@500;600;700;800&family=Fira+Sans:wght@700&family=Open+Sans:wght@600&family=Yellowtail&display=swap" rel="stylesheet">
<style>
  :root {
    --red: #ee2a1f;
    --black: #050505;
    --white: #ffffff;
    --tile: #5d5d5d;
    --tab: #6a6a6a;
    --stage: #dcdcdc;
  }
  * { margin: 0; padding: 0; box-sizing: border-box; }
  html, body { width: 852px; height: 1200px; overflow: hidden; }
  body { background: var(--stage); position: relative; font-family: "Montserrat", sans-serif; }

  .flyer {
    position: absolute; left: 125px; top: 148px;
    width: 602px; height: 903px;
    background: var(--white); overflow: hidden;
  }

  .hero-photo {
    position: absolute; left: 0; top: 0; width: 602px; height: 418px;
    background:
      linear-gradient(180deg, #3f6fae 0%, #8fb3dc 18%, #c9cfd6 30%, #9aa0a6 44%, #d8dcdf 56%, #b1aeaa 72%, #a6a39e 100%);
  }
  .hero-shade {
    position: absolute; left: 0; top: 0; width: 602px; height: 418px;
    background: linear-gradient(90deg, rgba(12,12,12,.98) 0%, rgba(18,18,18,.92) 34%, rgba(30,30,30,.55) 56%, rgba(40,40,40,0) 78%);
  }

  .brand {
    position: absolute; left: 38px; top: 41px;
    display: flex; align-items: center; gap: 8px;
  }
  .brand-mark { width: 14px; height: 14px; background: var(--red); }
  .brand-name { font-weight: 600; font-size: 21px; color: var(--white); letter-spacing: .2px; }

  .tagline-script {
    position: absolute; left: 35px; top: 88px;
    font-family: "Yellowtail", cursive; font-size: 31px; color: var(--red);
  }
  .headline {
    position: absolute; left: 34px; top: 130px;
    font-weight: 800; font-size: 43px; line-height: 49px; color: var(--white);
    letter-spacing: -.5px;
  }
  .headline-rule {
    position: absolute; left: 36px; top: 234px; width: 217px; height: 3px;
    background: linear-gradient(90deg, var(--red) 55%, rgba(238,42,31,0));
  }
  .lede {
    position: absolute; left: 36px; top: 250px;
    font-family: "Open Sans", sans-serif; font-weight: 600;
    font-size: 24px; line-height: 34px; color: var(--white);
    text-shadow: 0 1px 3px rgba(0,0,0,.6);
  }

  .services {
    position: absolute; left: 22px; top: 342px; width: 337px; height: 379px;
    background: var(--red);
    clip-path: polygon(0 0, 298px 0, 337px 39px, 337px 379px, 47px 379px, 0 332px);
  }
  .services-title {
    position: absolute; left: 41px; top: 22px;
    font-weight: 700; font-size: 28px; color: var(--white);
  }
  .services-rule {
    position: absolute; left: 42px; top: 61px; width: 141px; height: 1px; background: var(--white);
  }
  .services-rule::before {
    content: ""; position: absolute; left: 0; top: -1px; width: 85px; height: 2px; background: var(--white);
  }
  .service {
    position: absolute; left: 42px; display: flex; align-items: center; gap: 16px;
  }
  .service-icon {
    width: 57px; height: 52px; background: var(--tile);
    display: flex; align-items: center; justify-content: center;
  }
  .service-icon svg { width: 38px; height: 32px; }
  .service-label {
    font-family: "Fira Sans", sans-serif; font-weight: 700;
    font-size: 19px; line-height: 26px; color: var(--white);
  }

  .gallery {
    position: absolute; left: 370px; top: 342px; width: 216px; height: 333px;
    background: var(--white);
  }
  .gallery-photo {
    position: absolute; left: 7px; top: 8px; width: 203px; height: 318px;
    background: linear-gradient(180deg, #4d7fc0 0%, #a8c3e2 12%, #bfc4ca 24%, #8f959b 36%, #eceff1 48%, #d7d2d2 56%, #6c6c6c 62%, #b9b6b1 70%, #a7a49f 100%);
  }
  .gallery-split-v { position: absolute; left: 106px; top: 0; width: 4px; height: 333px; background: var(--white); }
  .gallery-split-h { position: absolute; left: 0; top: 164px; width: 216px; height: 4px; background: var(--white); }

  .accent-wedge {
    position: absolute; left: 0; top: 0; width: 602px; height: 903px; pointer-events: none;
  }

  .footer {
    position: absolute; left: 0; top: 759px; width: 602px; height: 144px; background: var(--black);
  }
  .contact-tab {
    position: absolute; left: 0; top: 757px; width: 240px; height: 56px;
    background: var(--tab);
    clip-path: polygon(0 0, 204px 0, 240px 56px, 0 56px);
  }
  .contact-title {
    position: absolute; left: 25px; top: 774px;
    font-weight: 700; font-size: 27px; color: #f2f2f2;
    text-shadow: 1px 2px 2px rgba(0,0,0,.55);
  }
  .email {
    position: absolute; left: 25px; top: 854px;
    display: flex; align-items: center; gap: 13px;
    font-weight: 500; font-size: 15px; color: var(--white);
  }
  .email svg { width: 20px; height: 14px; }
  .phone-icon { position: absolute; left: 317px; top: 800px; width: 20px; height: 20px; }
  .phones {
    position: absolute; left: 349px; top: 795px;
    list-style: none; font-weight: 600; font-size: 19.5px; line-height: 28px; color: var(--white);
  }
</style>
</head>
<body>
  <main class="flyer">
    <div class="hero-photo" role="img" aria-label="Photo of a white fuel tanker truck parked in front of a steel depot shed under a blue cloudy sky"></div>
    <div class="hero-shade"></div>

    <div class="brand">
      <span class="brand-mark"></span>
      <span class="brand-name">Terra Diesel</span>
    </div>

    <p class="tagline-script">We are a Bulk</p>
    <h1 class="headline">PETROLEUM<br>SUPPLIER</h1>
    <div class="headline-rule"></div>
    <p class="lede">Servicing any industry<br>that requires diesel</p>

    <section class="services">
      <h2 class="services-title">SERVICES</h2>
      <div class="services-rule"></div>

      <div class="service" style="top:86px">
        <div class="service-icon">
          <svg viewBox="0 0 38 32" fill="#fff"><rect x="2" y="8" width="22" height="12" rx="5"/><rect x="8" y="5" width="4" height="4"/><path d="M25 11h6l4 5v6H25z"/><rect x="2" y="20" width="33" height="2"/><circle cx="7" cy="24" r="3"/><circle cx="15" cy="24" r="3"/><circle cx="30" cy="24" r="3"/></svg>
        </div>
        <p class="service-label">Bulk Fuel<br>Deliveries</p>
      </div>

      <div class="service" style="top:156px">
        <div class="service-icon">
          <svg viewBox="0 0 38 32" fill="#fff"><rect x="16" y="2" width="6" height="4"/><path d="M12 8h14l2 4v18H10V12z"/><circle cx="23" cy="23" r="6" fill="#5d5d5d"/><path d="M23 18c2 3 3 4 3 5.5a3 3 0 0 1-6 0c0-1.5 1-2.5 3-5.5z"/></svg>
        </div>
        <p class="service-label">Oils &amp; Lubricants</p>
      </div>

      <div class="service" style="top:227px">
        <div class="service-icon">
          <svg viewBox="0 0 38 32" fill="#fff"><rect x="3" y="4" width="6" height="12"/><rect x="11" y="4" width="6" height="12"/><rect x="2" y="3" width="16" height="2"/><rect x="2" y="10" width="16" height="1.5"/><path d="M20 10h7l5 6v7H20z"/><rect x="2" y="17" width="30" height="5"/><circle cx="8" cy="25" r="3"/><circle cx="27" cy="25" r="3"/></svg>
        </div>
        <p class="service-label">Petrol Deliveries</p>
      </div>

      <div class="service" style="top:297px">
        <div class="service-icon">
          <svg viewBox="0 0 38 32" fill="#fff"><path d="M19 1l7 3v5c0 4-3 7-7 8-4-1-7-4-7-8V4z"/><path d="M16 8l2 2 4-4" stroke="#5d5d5d" stroke-width="1.6" fill="none"/><circle cx="9" cy="19" r="3"/><circle cx="29" cy="19" r="3"/><circle cx="19" cy="21" r="3"/><path d="M3 31v-4a5 5 0 0 1 10 0v4zM25 31v-4a5 5 0 0 1 10 0v4zM13 31v-2a6 6 0 0 1 12 0v2z"/></svg>
        </div>
        <p class="service-label">Local Family<br>Owned Business</p>
      </div>
    </section>

    <div class="gallery">
      <div class="gallery-photo" role="img" aria-label="Photo of a white fuel tanker trailer parked on concrete in front of a depot shed"></div>
      <div class="gallery-split-v"></div>
      <div class="gallery-split-h"></div>
    </div>

    <svg class="accent-wedge" viewBox="0 0 602 903"><polygon points="486,705 602,705 602,760 449,760" fill="#ee2a1f"/></svg>

    <footer class="footer"></footer>
    <div class="contact-tab"></div>
    <h2 class="contact-title">CONTACT US</h2>

    <div class="email">
      <svg viewBox="0 0 20 14"><rect width="20" height="14" fill="#ee2a1f"/><path d="M0 0l10 8 10-8M0 14l7-7M20 14l-7-7" stroke="#050505" stroke-width="1.3" fill="none"/></svg>
      <span>Fuel@terradiesel-example.com.au</span>
    </div>

    <svg class="phone-icon" viewBox="0 0 20 20"><path d="M4 2l3 0 2 5-2 1.5c1 2.5 3 4.5 5.5 5.5L14 12l5 2v3c0 1-1 2-2 2C9 18 2 11 2 4c0-1 1-2 2-2z" fill="#ee2a1f"/><path d="M12 2a6 6 0 0 1 6 6M12 5a3 3 0 0 1 3 3" stroke="#ee2a1f" stroke-width="1.5" fill="none"/></svg>
    <ul class="phones">
      <li>Marco - 0412 309 768</li>
      <li>Liam - 0431 672 095</li>
      <li>Simon - 0465 218 347</li>
    </ul>
  </main>
</body>
</html>
```